Direct Mail Postcard for new client solicitation

I need a postcard designed to market our full service accounting and financial services firm to local companies.

Our firm specializes in outsourced accounting and finance - we do everything from book keeping all the way up to financial oversight. We prefer to work on a flat fee recurring revenue basis rather than a traditional hourly fee. We also bring our own privately developed software to assist with the process. This software is proprietary in nature and not available elsewhere.

This card should convey:
1. Transferring financial headaches to a qualified company.
2. Stable access to help.
3. Cost savings.
4. A comprehensive package that allows for the client to take as much or as little as they would like.

I have attached our logo as a starting point. Feel free to engage us with questions and for guidance.

The company name is BrightLedgerPro.

Target Market(s)

the target market for this project is small businesses in the chicago area (our test market) with annual revenues between 5 and 10 Million dollars

Industry/Entity Type

Accounting

Font styles to use
Serif
Sans Serif

Requirements
Must have
• The project must convey the idea that we are taking administrative burdens and headaches from the client. The idea is that they are outsourcing their back office accounting functions to us while still retaining overall control of the process. The card must convey this concept somehow.
• We are also working on copy - since we are accountants and basically as boring as watching paint dry we are struggling a bit. Feel free to take a stab at copy as well. Keep in mind - we do not need to say alot - ideally we would say in essence "outsource your finance and accounting work to us for a reasonable fixed price".
Should not have
• We are reworking our website as well. The little orange guys and in fact the entire copy will be changing over the next few weeks. We would prefer to avoid using that motif for the card.

```html
<!DOCTYPE html>
<html lang="en">
<head>
<meta charset="utf-8">
<title>BrightLedgerPro Postcard</title>
<link href="https://fonts.googleapis.com/css2?family=Arimo:wght@400;700&display=swap" rel="stylesheet">
<style>
  :root {
    --page: #ecebe8;
    --card: #ffffff;
    --green: #3b6b3a;
    --steel: #335b82;
    --navy: #24415f;
    --lime: #b6bf3a;
    --tick: #e8b62f;
    --burst: #d8393a;
    --ink: #ffffff;
    --rule: #b9b9b9;
    --dark: #1a1a1a;
  }
  * { margin: 0; padding: 0; box-sizing: border-box; }
  html, body { width: 1200px; height: 1200px; overflow: hidden; }
  body { background: var(--page); font-family: "Arimo", Arial, sans-serif; position: relative; }

  .postcard {
    position: absolute; left: 50px; width: 1100px; height: 540px;
    background: var(--card); box-shadow: 0 2px 8px rgba(0,0,0,.18);
  }
  .postcard--back { top: 40px; }
  .postcard--front { top: 620px; }

  /* back side */
  .services-panel {
    position: absolute; left: 20px; top: 20px; width: 580px; height: 500px;
    background: var(--green); color: var(--ink); padding: 40px 0 0 70px;
  }
  .services-stripe { position: absolute; left: 600px; top: 20px; width: 40px; height: 500px; background: var(--steel); }
  .services-title { font-size: 28px; line-height: 36px; margin-left: 8px; }
  .services-list { list-style: none; }
  .services-list li { font-size: 27px; line-height: 33px; display: flex; align-items: center; gap: 8px; }
  .services-list svg { flex: none; }
  .services-tagline { font-size: 26px; line-height: 30px; margin-top: 22px; margin-left: -30px; }

  .stamp-box { position: absolute; right: 60px; top: 50px; width: 94px; height: 108px; border: 2px solid var(--dark); }
  .address-lines { position: absolute; left: 700px; top: 230px; width: 340px; }
  .address-lines span { display: block; height: 2px; background: var(--rule); margin-bottom: 34px; }

  /* front side */
  .pitch-panel {
    position: absolute; left: 20px; top: 20px; width: 540px; height: 500px;
    background: var(--navy); color: var(--ink); padding: 30px 30px 0 60px;
  }
  .pitch-stripe { position: absolute; left: 560px; top: 20px; width: 30px; height: 500px; background: var(--lime); }
  .headline { position: relative; font-size: 21px; line-height: 24px; }
  .headline-burst { position: absolute; left: -50px; top: -32px; }
  .headline-finally { position: relative; font-size: 40px; line-height: 44px; font-weight: 400; }
  .headline-rest { position: relative; }
  .pitch-body { font-size: 21px; line-height: 25.5px; margin-top: 22px; padding-left: 8px; }

  .brand { position: absolute; right: 50px; top: 56px; display: flex; align-items: center; gap: 10px; }
  .brand-name { font-size: 26px; font-weight: 700; color: var(--dark); letter-spacing: -0.5px; }
  .brand-mark { width: 24px; height: 24px; background: var(--steel); }

  .photo {
    position: absolute; left: 590px; top: 230px; width: 490px; height: 290px;
    background: linear-gradient(160deg, #f4f2ee 0%, #d8cfc2 40%, #5c5d66 70%, #e9e6e1 100%);
  }
</style>
</head>
<body>

<section class="postcard postcard--back">
  <div class="services-panel">
    <p class="services-title">We can help with</p>
    <ul class="services-list">
      <li><svg width="30" height="26" viewBox="0 0 30 26"><path d="M2 14 L10 22 L28 3" fill="none" stroke="var(--tick)" stroke-width="5" stroke-linecap="round"/></svg>Financial management</li>
      <li><svg width="30" height="26" viewBox="0 0 30 26"><path d="M2 14 L10 22 L28 3" fill="none" stroke="var(--tick)" stroke-width="5" stroke-linecap="round"/></svg>Accounting</li>
      <li><svg width="30" height="26" viewBox="0 0 30 26"><path d="M2 14 L10 22 L28 3" fill="none" stroke="var(--tick)" stroke-width="5" stroke-linecap="round"/></svg>Book keeping</li>
      <li><svg width="30" height="26" viewBox="0 0 30 26"><path d="M2 14 L10 22 L28 3" fill="none" stroke="var(--tick)" stroke-width="5" stroke-linecap="round"/></svg>Forecasting</li>
      <li><svg width="30" height="26" viewBox="0 0 30 26"><path d="M2 14 L10 22 L28 3" fill="none" stroke="var(--tick)" stroke-width="5" stroke-linecap="round"/></svg>Reporting</li>
      <li><svg width="30" height="26" viewBox="0 0 30 26"><path d="M2 14 L10 22 L28 3" fill="none" stroke="var(--tick)" stroke-width="5" stroke-linecap="round"/></svg>Bank management</li>
      <li><svg width="30" height="26" viewBox="0 0 30 26"><path d="M2 14 L10 22 L28 3" fill="none" stroke="var(--tick)" stroke-width="5" stroke-linecap="round"/></svg>Fund raising</li>
      <li><svg width="30" height="26" viewBox="0 0 30 26"><path d="M2 14 L10 22 L28 3" fill="none" stroke="var(--tick)" stroke-width="5" stroke-linecap="round"/></svg>Business transition planning</li>
      <li><svg width="30" height="26" viewBox="0 0 30 26"><path d="M2 14 L10 22 L28 3" fill="none" stroke="var(--tick)" stroke-width="5" stroke-linecap="round"/></svg>Tax compliance</li>
    </ul>
    <p class="services-tagline">If you have headaches we have<br>solutions!</p>
  </div>
  <div class="services-stripe"></div>
  <div class="stamp-box"></div>
  <div class="address-lines"><span></span><span></span><span></span><span></span><span></span></div>
</section>

<section class="postcard postcard--front">
  <div class="pitch-panel">
    <p class="headline">
      <svg class="headline-burst" width="240" height="100" viewBox="0 0 240 100">
        <polygon fill="var(--burst)" points="0,40 60,38 40,8 95,28 125,0 140,30 200,18 175,45 240,58 170,64 190,96 130,74 100,100 88,72 30,86 58,58"/>
      </svg>
      <span class="headline-finally">Finally</span><span class="headline-rest"> - a way to outsource<br>those financial headaches without<br>losing control!</span>
    </p>
    <p class="pitch-body">BrightLedgerPro is more than a consulting firm - we are a partner that provides a total solution for all your financial headaches. BrightLedgerPro is revolutionary way to handle your businesses finances. Using proprietary tools that allow you to control and monitor the processing of data we provide the most comprehensive solution to all your accounting and finance issues! Now you can move just the issues you want - at prices you can afford.</p>
  </div>
  <div class="pitch-stripe"></div>
  <div class="brand"><span class="brand-name">BrightLedgerPro</span><span class="brand-mark"></span></div>
  <div class="photo" role="img" aria-label="Photo of an exhausted businessman resting his head on a desk beside a tall stack of books and open papers"></div>
</section>

</body>
</html>
```